Plumbing business card and logo desgin

Need a new business card and logo for a plumbing business based in Warragul, Australia. Business name is 7Kelby plumbing & air-conditioning. We service all plumbing and gasfitting needs and installation of air-conditioning. We clear blocked drains, install new hot water systems, central heating, new and existing homes, roofing, sanitary and drainage.
i would like to have a space on there for website, email, phone, licence number and what we do as a company.
i would like a water droplet to be incorporated into the design to try and stand out that we are a plumbing business

Contact Information for Business Card

website:
phone number: 0458271936
Licence Number: 382716

Logo Text

7Kelby Plumbing & Air-Conditioning

```html
<!DOCTYPE html>
<html lang="en">
<head>
<meta charset="UTF-8">
<title>7Kelby Plumbing &amp; Air-Conditioning – Business Card</title>
<link href="https://fonts.googleapis.com/css2?family=Barlow:wght@300;500;600;700&display=swap" rel="stylesheet">
<style>
  :root {
    --navy: #22405c;
    --water: #4f8fc0;
    --ink: #2e2e2e;
    --paper: #ffffff;
    --drop-pale: #e6eff8;
    --drop-mid: #c9dcee;
  }
  html, body {
    margin: 0;
    padding: 0;
    overflow: hidden;
    background: var(--paper);
  }
  .card {
    position: relative;
    width: 1200px;
    height: 800px;
    overflow: hidden;
    background: var(--paper);
    font-family: "Barlow", Arial, sans-serif;
    color: var(--ink);
  }
  .droplet-band {
    position: absolute;
    left: 0;
    width: 1200px;
  }
  .droplet-band--top {
    top: 0;
    height: 195px;
    background: linear-gradient(180deg, var(--drop-mid) 0%, var(--drop-pale) 55%, rgba(255,255,255,0) 100%);
  }
  .droplet-band--bottom {
    bottom: 0;
    height: 195px;
    background: linear-gradient(0deg, var(--drop-mid) 0%, var(--drop-pale) 55%, rgba(255,255,255,0) 100%);
  }
  .side-bar {
    position: absolute;
    left: 0;
    top: 217px;
    width: 87px;
    height: 359px;
    background: var(--navy);
  }
  .holder {
    position: absolute;
    left: 124px;
    top: 250px;
  }
  .holder__name {
    margin: 0;
    font-size: 52px;
    font-weight: 700;
    letter-spacing: 1px;
    line-height: 1;
    color: var(--ink);
    text-transform: uppercase;
  }
  .holder__role {
    margin: 4px 0 0;
    font-size: 30px;
    font-weight: 300;
    letter-spacing: 0.5px;
    line-height: 1;
    text-transform: uppercase;
  }
  .divider {
    position: absolute;
    left: 129px;
    top: 372px;
    width: 346px;
    height: 1px;
    background: var(--ink);
  }
  .contact-list {
    position: absolute;
    left: 124px;
    top: 390px;
    margin: 0;
    padding: 0;
    list-style: none;
  }
  .contact-list__item {
    display: flex;
    align-items: center;
    height: 24px;
    margin-bottom: 13px;
    font-size: 20px;
    font-weight: 600;
    letter-spacing: 0.5px;
    text-transform: uppercase;
    white-space: nowrap;
  }
  .contact-list__icon {
    width: 24px;
    height: 24px;
    margin-right: 18px;
    flex: none;
  }
  .brand {
    position: absolute;
    left: 680px;
    top: 228px;
    width: 420px;
    text-align: center;
    color: var(--navy);
  }
  .brand__mark {
    display: block;
    width: 110px;
    height: 110px;
    margin: 0 auto 20px;
    border-radius: 50%;
    background: var(--navy);
  }
  .brand__name {
    margin: 0;
    font-size: 30px;
    font-weight: 600;
    line-height: 1.2;
    color: var(--navy);
  }
  .services {
    display: flex;
    align-items: flex-start;
    justify-content: center;
    margin: 18px auto 0;
    width: 400px;
    font-size: 15px;
    font-weight: 500;
    line-height: 1.35;
    color: var(--ink);
    text-align: left;
  }
  .services__drop {
    width: 18px;
    height: 26px;
    margin-right: 10px;
    flex: none;
  }
</style>
</head>
<body>
  <div class="card">
    <div class="droplet-band droplet-band--top" role="img" aria-label="Scattered water droplets and bubbles along the top edge"></div>
    <div class="droplet-band droplet-band--bottom" role="img" aria-label="Scattered water droplets and bubbles along the bottom edge"></div>

    <div class="side-bar"></div>

    <div class="holder">
      <h1 class="holder__name">Marlowe Tennant</h1>
      <p class="holder__role">Project Director</p>
    </div>

    <div class="divider"></div>

    <ul class="contact-list">
      <li class="contact-list__item">
        <svg class="contact-list__icon" viewBox="0 0 28 28" aria-hidden="true">
          <path d="M14 3c-4.4 0-8 3.5-8 7.9C6 16.8 14 25 14 25s8-8.2 8-14.1C22 6.5 18.4 3 14 3zm0 10.8a3 3 0 1 1 0-6 3 3 0 0 1 0 6z" fill="var(--ink)"/>
        </svg>
        Main Road, Warragul, Australia
      </li>
      <li class="contact-list__item">
        <svg class="contact-list__icon" viewBox="0 0 28 28" aria-hidden="true">
          <rect x="8" y="2" width="12" height="24" rx="2" fill="var(--ink)"/>
          <rect x="10" y="5" width="8" height="15" fill="var(--paper)"/>
          <circle cx="14" cy="23" r="1.2" fill="var(--paper)"/>
        </svg>
        0458 271 936
      </li>
      <li class="contact-list__item">
        <svg class="contact-list__icon" viewBox="0 0 28 28" aria-hidden="true">
          <rect x="3" y="7" width="22" height="15" rx="1.5" fill="var(--ink)"/>
          <path d="M3.5 8 14 16 24.5 8" fill="none" stroke="var(--paper)" stroke-width="2"/>
        </svg>
        marlowe@7kelbyplumbing.com.au
      </li>
      <li class="contact-list__item">
        <svg class="contact-list__icon" viewBox="0 0 28 28" aria-hidden="true">
          <circle cx="14" cy="14" r="10" fill="none" stroke="var(--ink)" stroke-width="2"/>
          <ellipse cx="14" cy="14" rx="4.5" ry="10" fill="none" stroke="var(--ink)" stroke-width="2"/>
          <path d="M4 14h20" stroke="var(--ink)" stroke-width="2"/>
        </svg>
        www.7kelbyplumbing.com.au
      </li>
      <li class="contact-list__item">
        <svg class="contact-list__icon" viewBox="0 0 28 28" aria-hidden="true">
          <rect x="3" y="6" width="22" height="16" rx="2" fill="var(--ink)"/>
          <circle cx="10" cy="13" r="3" fill="var(--paper)"/>
          <rect x="15" y="11" width="7" height="2" fill="var(--paper)"/>
          <rect x="15" y="15" width="7" height="2" fill="var(--paper)"/>
        </svg>
        Licence No. 382716
      </li>
    </ul>

    <div class="brand">
      <span class="brand__mark" aria-hidden="true"></span>
      <p class="brand__name">7Kelby<br>Plumbing &amp; Air-Conditioning</p>
      <div class="services">
        <svg class="services__drop" viewBox="0 0 18 26" aria-hidden="true">
          <path d="M9 1C9 1 1 12 1 17a8 8 0 0 0 16 0C17 12 9 1 9 1z" fill="var(--water)"/>
        </svg>
        <span>Plumbing &amp; gasfitting · Blocked drains · Hot water systems · Central heating · Roofing · Sanitary &amp; drainage · Air-conditioning</span>
      </div>
    </div>
  </div>
</body>
</html>
```